Design Challege - Simplify a Complex Message

We have a new website design, but one of the pages presents a particular problem.

Our company does ERP implementations. We have developed a proprietary approach to these implementations based on the idea that you must get eight (and only eight) things right. These eight things are listed below, summarized in one or two words each:

1. Value
2. Capability
3. Functionality
4. Data
5. Technology
6. Change Leadership
7. Quality
8. Governance

Each of these eight things can be summarized in a short paragraph, but when you combine all eight summaries with a brief introductory text, the result is a lot of text - so much text that the casual surfer may be overwhelmed by it.

The winning design will find an engaging way to present the information in a way that presents a high-level summary, using icons and one- or two-word descriptions above but revealing more information when clicked.

Our current design for this information, with a paragraph describing the eight elements in a table, is included as an upload in PDF and Microsoft Word formats. We are looking for a creative way to display these eight things, showing the detail only when the user wants to see it.

The website is being built in WordPress, using Elementor as a page builder.

We will implement (code) the page, but the winner will be asked to specify the widget or other add-in if one is required.

The design does not need to include a header or footer, we have those.

Target Market(s)

Business executives working in technology

Industry/Entity Type

Any

Number of Pages Required

1 page

Font styles to use
Sans Serif

Requirements
Must have
• A design for the body of the page, but not the header or footer.
Nice to have
• Unique icons or images appropriate for each of the eight things.
Should not have
• A lot of text on one page

```html
<!DOCTYPE html>
<html lang="en">
<head>
<meta charset="utf-8">
<title>ERP Implementations – Eight Things to Get Right</title>
<link href="https://fonts.googleapis.com/css2?family=Open+Sans:wght@400;700;800&family=Exo+2:wght@700;800&family=Lato:wght@400;700&display=swap" rel="stylesheet">
<style>
  :root{
    --ink:#0d0d0d;
    --text:#2b2b2b;
    --muted:#5f6268;
    --label:#4d5056;
    --panel:#f1f4fb;
    --card:#ffffff;
    --value-a:#ffc400; --value-b:#f0701b;
    --cap-a:#ffa51a; --cap-b:#ee5a16;
    --func-a:#84cc6a; --func-b:#1f8a3a;
    --data-a:#5ccad8; --data-b:#1a94a8;
    --tech-a:#3b6ea8; --tech-b:#1e3f73;
    --change-a:#8794b0; --change-b:#4c5878;
    --qual-a:#f68cc0; --qual-b:#e0357f;
    --gov-a:#b8834f; --gov-b:#7a4b22;
  }
  *{box-sizing:border-box;margin:0;padding:0}
  html,body{width:712px;height:1200px;overflow:hidden;background:#fff}
  body{position:relative;font-family:"Lato",sans-serif;color:var(--text)}
  .page-title{position:absolute;top:40px;left:0;width:712px;text-align:center;
    font-family:"Open Sans",sans-serif;font-weight:800;font-size:32px;color:var(--ink);letter-spacing:.3px}
  .page-subtitle{position:absolute;top:96px;left:0;width:712px;text-align:center;
    font-family:"Open Sans",sans-serif;font-weight:400;font-size:18.5px;color:var(--ink)}
  .intro{position:absolute;top:136px;left:106px;width:500px;text-align:center;
    font-family:"Open Sans",sans-serif;font-size:9.6px;line-height:20.3px;color:var(--text)}
  .panel{position:absolute;top:242px;left:66px;width:579px;height:918px;background:var(--panel);border-radius:10px}
  .card{position:absolute;left:110px;width:491px;height:89px;background:var(--card);
    box-shadow:0 4px 8px rgba(40,50,80,.08)}
  .card.odd{background:linear-gradient(90deg,rgba(255,255,255,0) 0%,#fff 18%)}
  .card.even{background:linear-gradient(90deg,#fff 75%,rgba(255,255,255,.3) 100%)}
  .accent{position:absolute;top:0;width:19px;height:89px}
  .odd .accent{right:0;border-radius:0 3px 3px 0}
  .even .accent{left:0;border-radius:3px 0 0 3px}
  .badge{position:absolute;top:12px;width:64px;height:64px;border-radius:50%}
  .odd .badge{left:375px}
  .even .badge{left:43px}
  .heading{position:absolute;top:0;height:89px;display:flex;flex-direction:column;
    align-items:center;justify-content:center;text-align:center}
  .odd .heading{left:-8px;width:112px}
  .even .heading{left:108px;width:100px}
  .num{font-family:"Exo 2",sans-serif;font-weight:800;font-size:30px;line-height:32px;color:var(--label)}
  .label{font-family:"Exo 2",sans-serif;font-weight:700;font-size:11.2px;line-height:20px;color:var(--label);letter-spacing:.4px;margin-top:2px}
  .summary{position:absolute;top:12px;font-size:7.9px;line-height:16.3px;color:var(--muted)}
  .odd .summary{left:105px;width:250px}
  .even .summary{left:219px;width:250px}
  .summary a{color:var(--label);font-weight:700;text-decoration:underline}

  .c1{top:283px}.c2{top:387px}.c3{top:491px}.c4{top:598px}
  .c5{top:705px}.c6{top:808px}.c7{top:912px}.c8{top:1020px}

  .c1 .accent{background:linear-gradient(180deg,var(--value-b),var(--value-a))}
  .c1 .badge{background:radial-gradient(circle at 30% 30%,var(--value-a),var(--value-b))}
  .c2 .accent{background:linear-gradient(90deg,var(--cap-b),var(--cap-a))}
  .c2 .badge{background:radial-gradient(circle at 30% 30%,var(--cap-a),var(--cap-b))}
  .c3 .accent{background:linear-gradient(90deg,var(--func-b),var(--func-a))}
  .c3 .badge{background:radial-gradient(circle at 30% 30%,var(--func-a),var(--func-b))}
  .c4 .accent{background:linear-gradient(90deg,var(--data-a),var(--data-b))}
  .c4 .badge{background:radial-gradient(circle at 30% 30%,var(--data-a),var(--data-b))}
  .c5 .accent{background:linear-gradient(90deg,var(--tech-a),var(--tech-b))}
  .c5 .badge{background:radial-gradient(circle at 30% 30%,var(--tech-a),var(--tech-b))}
  .c6 .accent{background:linear-gradient(90deg,var(--change-b),var(--change-a))}
  .c6 .badge{background:radial-gradient(circle at 30% 30%,var(--change-a),var(--change-b))}
  .c7 .accent{background:linear-gradient(90deg,var(--qual-b),var(--qual-a))}
  .c7 .badge{background:radial-gradient(circle at 30% 30%,var(--qual-a),var(--qual-b))}
  .c8 .accent{background:linear-gradient(90deg,var(--gov-b),var(--gov-a))}
  .c8 .badge{background:radial-gradient(circle at 30% 30%,var(--gov-a),var(--gov-b))}
</style>
</head>
<body>
  <h1 class="page-title">ERP Implementations</h1>
  <h2 class="page-subtitle">Eight Things to Get Right</h2>
  <p class="intro">Like the roots and branches of a tree, there are many considerations in an ERP implementation. Focus too much on the minor details, and you can lose sight of the tree. In an ERP implementation, you must get eight major things right to be successful. Ignore any of them, and your implementation will fail. Get them right, and you will likely succeed.</p>

  <div class="panel"></div>

  <section class="card odd c1">
    <div class="heading"><span class="num">01</span><span class="label">VALUE</span></div>
    <p class="summary">The project must provide value that significantly exceeds potential project costs and should be aligned with the company's strategy. Its value and strategic alignment must be part of a vision shared by the company's leadership......<a href="#">Learn More</a></p>
    <div class="badge" role="img" aria-label="Icon: hands holding a person under three stars"></div>
    <div class="accent"></div>
  </section>

  <section class="card even c2">
    <div class="accent"></div>
    <div class="badge" role="img" aria-label="Icon: light bulb with gear and rising arrows"></div>
    <div class="heading"><span class="num">02</span><span class="label">CAPABILITY</span></div>
    <p class="summary">The company and the implementation team must be capable of implementing the project on their own or with help. The project must have the following:• Resources required, including people, time, and budget.......<a href="#">Learn More</a></p>
  </section>

  <section class="card odd c3">
    <div class="heading"><span class="num">03</span><span class="label">FUNCTIONALITY</span></div>
    <p class="summary">An ERP project must support required business processes, both now and in the future. A systematic review of all business processes and how they will be supported, either by the system or otherwise, is crucial.......<a href="#">Learn More</a></p>
    <div class="badge" role="img" aria-label="Icon: monitor with gears"></div>
    <div class="accent"></div>
  </section>

  <section class="card even c4">
    <div class="accent"></div>
    <div class="badge" role="img" aria-label="Icon: data dashboard with charts"></div>
    <div class="heading"><span class="num">04</span><span class="label">DATA</span></div>
    <p class="summary">The company and the implementation team must be capable of implementing the project on their own or with help. The project must have the following:• Resources required, including people, time, and budget.......<a href="#">Learn More</a></p>
  </section>

  <section class="card odd c5">
    <div class="heading"><span class="num">05</span><span class="label">TECHNOLOGY</span></div>
    <p class="summary">The project must provide value that significantly exceeds potential project costs and should be aligned with the company's strategy. Its value and strategic alignment must be part of a vision shared by the company's leadership......<a href="#">Learn More</a></p>
    <div class="badge" role="img" aria-label="Icon: gears inside a light bulb"></div>
    <div class="accent"></div>
  </section>

  <section class="card even c6">
    <div class="accent"></div>
    <div class="badge" role="img" aria-label="Icon: group of people with shuffle arrows"></div>
    <div class="heading"><span class="num">06</span><span class="label">CHANGE<br>LEADERSHIP</span></div>
    <p class="summary">Change leadership (often called change management) considers the human side of an ERP implementation. Change is hard, even if it's a good change. Training is an important element of change leadership. .......<a href="#">Learn More</a></p>
  </section>

  <section class="card odd c7">
    <div class="heading"><span class="num">07</span><span class="label">QUALITY</span></div>
    <p class="summary">Quality is multi-dimensional, and it's more than a measurement; it's a perception. An ERP needs to be reliable. But poor performance or poor user experience are often root causes of implementation failure........<a href="#">Learn More</a></p>
    <div class="badge" role="img" aria-label="Icon: thumbs up badge under three stars"></div>
    <div class="accent"></div>
  </section>

  <section class="card even c8">
    <div class="accent"></div>
    <div class="badge" role="img" aria-label="Icon: handshake with team and gear"></div>
    <div class="heading"><span class="num">08</span><span class="label">GOVERNANCE</span></div>
    <p class="summary">ERP projects require both management and leadership. Planning, changing plans, communication, decision making, and guidance are critical aspects of management........<a href="#">Learn More</a></p>
  </section>
</body>
</html>
```